We need a business card design for a Dubai based company .

We need a business card for a Dubai based company called "Marwaneq Smoking Requisites Trading LLC". We mainly import Flavoured Tobacco products and Charcoal which is used for smoking in a Hookah/Shisha and distribute to the wholesalers and retailers. Logo file is attached herewith.

```html
<!DOCTYPE html>
<html lang="en">
<head>
<meta charset="utf-8">
<title>Marwaneq Business Card</title>
<link href="https://fonts.googleapis.com/css2?family=Poppins:wght@300;400;500;600&display=swap" rel="stylesheet">
<style>
  :root {
    --page: #e9eaec;
    --card-dark: #121212;
    --card-light: #ffffff;
    --accent: #c8363a;
    --text-dark: #2a2a2a;
    --text-muted: #6e6e6e;
    --text-light: #f2f2f2;
  }
  * { margin: 0; padding: 0; box-sizing: border-box; }
  html, body {
    width: 1200px; height: 1200px; overflow: hidden;
    background: var(--page);
    font-family: "Poppins", sans-serif;
  }
  .canvas { position: relative; width: 1200px; height: 1200px; }
  .card {
    position: absolute; left: 180px; width: 840px; height: 480px;
    box-shadow: 0 14px 34px rgba(0,0,0,0.16);
  }
  .card--front { top: 90px; background: var(--card-dark); border-bottom: 6px solid var(--accent); }
  .card--back { top: 630px; background: var(--card-light); }

  .brand__name {
    display: block; font-weight: 500; letter-spacing: 0.08em;
    text-transform: uppercase; line-height: 1.3;
  }
  .card--front .brand__name {
    position: absolute; left: 50%; top: 50%; transform: translate(-50%, -50%);
    width: 520px; text-align: center; color: var(--text-light); font-size: 28px;
  }
  .card--back .brand__name {
    position: absolute; left: 60px; top: 88px; width: 300px;
    color: var(--text-dark); font-size: 19px;
  }

  .person { position: absolute; right: 60px; top: 70px; text-align: right; }
  .person__name { font-size: 30px; font-weight: 600; letter-spacing: 0.04em; color: var(--text-dark); text-transform: uppercase; }
  .person__role { font-size: 17px; font-weight: 400; color: var(--accent); margin-top: 2px; }
  .person__rule { position: absolute; right: 60px; top: 160px; width: 370px; height: 2px; background: var(--accent); }

  .address { position: absolute; right: 60px; top: 200px; text-align: right; font-style: normal; font-size: 17px; font-weight: 300; line-height: 1.45; color: var(--text-muted); }

  .contact-rule { position: absolute; left: 60px; top: 318px; width: 420px; height: 1.5px; background: var(--accent); }
  .contacts { position: absolute; left: 60px; top: 336px; list-style: none; }
  .contacts__item { display: flex; align-items: center; gap: 14px; font-size: 16px; font-weight: 300; color: var(--text-dark); height: 27px; }
  .contacts__icon { width: 15px; height: 15px; flex: none; }
</style>
</head>
<body>
<main class="canvas">

  <section class="card card--front" aria-label="Card front">
    <span class="brand__name">Marwaneq Smoking Requisites Trading LLC</span>
  </section>

  <section class="card card--back" aria-label="Card back">
    <span class="brand__name">Marwaneq Smoking Requisites Trading LLC</span>

    <div class="person">
      <p class="person__name">Daniel Harper</p>
      <p class="person__role">Managing Director</p>
    </div>
    <div class="person__rule"></div>

    <address class="address">
      Al Wasl Road<br>PO Box 40218<br>Jumeirah Dubai
    </address>

    <div class="contact-rule"></div>
    <ul class="contacts">
      <li class="contacts__item">
        <svg class="contacts__icon" viewBox="0 0 16 16"><path fill="#c8363a" d="M3.5 1.5l2.5 0 1 3.5-1.6 1.2c.8 1.8 2.2 3.2 4 4l1.2-1.6 3.4 1v2.6c0 .7-.6 1.3-1.3 1.3C7.3 13.5 2.5 8.7 2.2 2.8c0-.7.6-1.3 1.3-1.3z"/></svg>
        +971 4 555 0142
      </li>
      <li class="contacts__item">
        <svg class="contacts__icon" viewBox="0 0 16 16"><rect x="4" y="1" width="8" height="14" rx="1.5" fill="none" stroke="#c8363a" stroke-width="1.6"/><circle cx="8" cy="12.3" r="0.9" fill="#c8363a"/></svg>
        +971 4 555 0142
      </li>
      <li class="contacts__item">
        <svg class="contacts__icon" viewBox="0 0 16 16"><rect x="1" y="3" width="14" height="10" rx="1" fill="#c8363a"/><path d="M1.5 3.8L8 9l6.5-5.2" fill="none" stroke="#fff" stroke-width="1.3"/></svg>
        info@marwaneqsmoking.com
      </li>
      <li class="contacts__item">
        <svg class="contacts__icon" viewBox="0 0 16 16"><circle cx="8" cy="8" r="6.6" fill="none" stroke="#c8363a" stroke-width="1.5"/><ellipse cx="8" cy="8" rx="2.8" ry="6.6" fill="none" stroke="#c8363a" stroke-width="1.2"/><path d="M1.5 8h13" stroke="#c8363a" stroke-width="1.2"/></svg>
        www.marwaneqsmoking.com
      </li>
    </ul>
  </section>

</main>
</body>
</html>
```